Folder Graphic Design for Water Technology Exhibition

Design the front cover of a folder that will be used as a handout during a water technology exhibition.

```html
<!DOCTYPE html>
<html lang="en">
<head>
<meta charset="UTF-8">
<title>Folder Cover – High Efficiency Engineered</title>
<link rel="stylesheet" href="https://fonts.googleapis.com/css2?family=Montserrat:wght@700;800&display=swap">
<style>
  :root {
    --blue-deep: #0a8ecb;
    --blue-mid: #2fb0e6;
    --blue-light: #5ccbf4;
    --plan-tint: rgba(255, 255, 255, 0.10);
    --frame: #8fd6f5;
    --white: #ffffff;
    --brand-blue: #1ea8e2;
    --partner-blue: #1c5aa6;
  }
  html, body {
    margin: 0;
    padding: 0;
    width: 848px;
    height: 1200px;
    overflow: hidden;
    background: var(--white);
  }
  .cover {
    position: relative;
    width: 848px;
    height: 1200px;
    overflow: hidden;
    box-sizing: border-box;
    border: 4px solid var(--frame);
    background: var(--white);
    font-family: "Montserrat", sans-serif;
  }
  .cover__backdrop {
    position: absolute;
    inset: 0;
    background: linear-gradient(180deg, var(--blue-deep) 0%, var(--blue-mid) 45%, var(--blue-light) 85%);
  }
  .cover__site-plan {
    position: absolute;
    left: 0;
    top: 120px;
    width: 840px;
    height: 800px;
    background:
      radial-gradient(ellipse 60% 45% at 50% 45%, var(--plan-tint) 0%, rgba(255, 255, 255, 0.04) 60%, rgba(255, 255, 255, 0) 100%);
  }
  .cover__title {
    position: absolute;
    top: 160px;
    left: 0;
    width: 840px;
    margin: 0;
    text-align: center;
    color: var(--white);
    font-weight: 700;
    font-size: 73px;
    line-height: 80px;
    letter-spacing: 0.5px;
    white-space: nowrap;
  }
  .cover__rule {
    position: absolute;
    top: 337px;
    left: 150px;
    width: 540px;
    border-top: 1px dashed rgba(255, 255, 255, 0.8);
  }
  .cover__wave {
    position: absolute;
    left: 0;
    top: 0;
    width: 840px;
    height: 1192px;
  }
  .footer__group {
    position: absolute;
    top: 1010px;
    left: 0;
    width: 840px;
    margin: 0;
    text-align: center;
    color: var(--brand-blue);
    font-weight: 800;
    font-size: 40px;
    line-height: 41px;
  }
  .partner {
    position: absolute;
    top: 1028px;
    width: 110px;
    display: flex;
    flex-direction: column;
    align-items: center;
    gap: 8px;
    color: var(--partner-blue);
    font-weight: 800;
    font-size: 18px;
    line-height: 22px;
  }
  .partner__mark {
    width: 70px;
    height: 70px;
    border-radius: 50%;
    background: var(--partner-blue);
  }
  .partner--left { left: 113px; }
  .partner--right { left: 630px; }
</style>
</head>
<body>
  <div class="cover">
    <div class="cover__backdrop"></div>
    <div class="cover__site-plan" role="img" aria-label="Faint engineering site plan of water treatment basins and pipelines behind the cover"></div>

    <h1 class="cover__title">HIGH EFFICIENCY<br>ENGINEERED</h1>
    <div class="cover__rule"></div>

    <svg class="cover__wave" viewBox="0 0 840 1192" aria-hidden="true">
      <path d="M0 940 C 50 920, 120 912, 210 918 C 410 932, 620 960, 840 986 L840 1192 L0 1192 Z" fill="#ffffff"/>
    </svg>

    <div class="partner partner--left">
      <span class="partner__mark"></span>
      <span class="partner__name">Aqualine</span>
    </div>

    <p class="footer__group">CLEARSTREAM<br>CAPITAL<br>PARTNERS</p>

    <div class="partner partner--right">
      <span class="partner__mark"></span>
      <span class="partner__name">PureBind</span>
    </div>
  </div>
</body>
</html>
```